Valtesh Spinal Care and Performance

We need new business cards, something more modern, clean. On the back of the card maybe a quote. The Dr. likes, “The doctor of the future will give no medicine, but will interest his patient in the care of the human frame, in diet and in the cause and prevention of disease.” - Walter Pimsley. We are open to other suggestions. We are a chiropractic office.

```html
<!DOCTYPE html>
<html lang="en">
<head>
<meta charset="utf-8">
<title>Valtesh Spinal Care and Performance – Business Card</title>
<link href="https://fonts.googleapis.com/css2?family=Libre+Baskerville:wght@700&family=Roboto:wght@400;500&display=swap" rel="stylesheet">
<style>
  :root {
    --backdrop: #d6d6d6;
    --card-white: #ffffff;
    --brand-purple: #5c2a63;
    --brand-purple-soft: #6b3a72;
    --brand-green: #8aa52d;
    --text-grey: #8b8b8b;
    --shadow: rgba(0, 0, 0, 0.22);
  }
  * { box-sizing: border-box; margin: 0; padding: 0; }
  html, body {
    width: 1200px; height: 852px; overflow: hidden;
    background: var(--backdrop);
    font-family: "Roboto", Arial, sans-serif;
  }
  .canvas { position: relative; width: 1200px; height: 852px; }

  .card {
    position: absolute;
    width: 620px; height: 355px;
    border-radius: 22px;
    overflow: hidden;
    box-shadow: 0 8px 18px var(--shadow);
  }

  /* Back of card */
  .card--back {
    left: 60px; top: 50px;
    background: var(--brand-purple);
    color: #fff;
    display: flex; flex-direction: column; justify-content: center;
    padding: 0 56px;
  }
  .quote {
    font-size: 17px; line-height: 1.6; font-weight: 400;
    text-align: center;
  }
  .quote-mark { color: var(--brand-green); }
  .quote-author {
    margin-top: 26px;
    text-align: right;
    color: var(--brand-green);
    font-size: 16px; font-weight: 500;
  }

  /* Front of card */
  .card--front {
    left: 520px; top: 440px;
    background: var(--card-white);
  }
  .front-band {
    position: absolute; left: 0; right: 0; bottom: 0;
    height: 22px; background: var(--brand-purple);
  }
  .brand {
    position: absolute; left: 42px; top: 40px;
    display: flex; align-items: center; gap: 10px;
  }
  .brand-dot {
    width: 16px; height: 16px; border-radius: 50%;
    background: var(--brand-green);
  }
  .brand-name {
    font-family: "Libre Baskerville", Georgia, serif;
    font-weight: 700; font-size: 26px;
    color: var(--brand-purple);
    letter-spacing: 1px;
  }
  .details { position: absolute; left: 42px; top: 140px; }
  .person-name {
    font-family: "Libre Baskerville", Georgia, serif;
    font-weight: 700; font-size: 24px;
    color: var(--brand-green);
    letter-spacing: 1px;
  }
  .person-role {
    margin-top: 4px;
    font-size: 17px; color: var(--text-grey);
    padding-bottom: 6px;
    border-bottom: 2px solid var(--brand-purple);
    display: inline-block; width: 72px;
  }
  .address {
    margin-top: 10px; font-size: 16px; line-height: 1.3;
    color: var(--text-grey); font-style: normal;
  }
  .contact-list { list-style: none; margin-top: 8px; }
  .contact-item {
    display: flex; align-items: center; gap: 8px;
    font-size: 16px; line-height: 1.5; color: var(--text-grey);
  }
  .contact-item--web { color: var(--brand-purple); font-weight: 500; }
  .contact-icon { width: 13px; height: 13px; fill: var(--brand-purple); flex: none; }
</style>
</head>
<body>
<main class="canvas">

  <section class="card card--back" aria-label="Card back">
    <p class="quote"><span class="quote-mark">“</span>The doctor of the future will give no medicine, but will interest his patient in the care of the human frame, in diet and in the cause and prevention of disease.<span class="quote-mark">”</span></p>
    <p class="quote-author">- Walter Pimsley</p>
  </section>

  <section class="card card--front" aria-label="Card front">
    <div class="brand">
      <span class="brand-dot"></span>
      <span class="brand-name">Valtesh</span>
    </div>

    <div class="details">
      <h1 class="person-name">Maren Holloway</h1>
      <p class="person-role">Doctor</p>
      <address class="address">Suite 4, 18 Corella Street<br>BRAVELLE NSW 2188</address>
      <ul class="contact-list">
        <li class="contact-item">
          <svg class="contact-icon" viewBox="0 0 24 24" aria-hidden="true"><path d="M6.6 10.8a15.1 15.1 0 0 0 6.6 6.6l2.2-2.2c.3-.3.7-.4 1-.2 1.1.4 2.3.6 3.6.6.6 0 1 .4 1 1V20c0 .6-.4 1-1 1A17 17 0 0 1 3 4c0-.6.4-1 1-1h3.5c.6 0 1 .4 1 1 0 1.3.2 2.5.6 3.6.1.3 0 .7-.2 1z"/></svg>
          (02) 5550 1847
        </li>
        <li class="contact-item">
          <svg class="contact-icon" viewBox="0 0 24 24" aria-hidden="true"><path d="M2 5h20v14H2z M3 6l9 7 9-7" stroke="#fff" stroke-width="1.5"/></svg>
          maren.holloway@valteshspinal.com.au
        </li>
        <li class="contact-item contact-item--web">
          <svg class="contact-icon" viewBox="0 0 24 24" aria-hidden="true"><circle cx="12" cy="12" r="10"/></svg>
          www.valteshspinal.com.au
        </li>
      </ul>
    </div>

    <div class="front-band"></div>
  </section>

</main>
</body>
</html>
```